Corvane Stationery Design

We need design for our stationary, including:
1) Letterhead
- A4/Letter size in landscape and portrait letterhead
- The letterhead must be in a word file, and the address should be editable using the Felixti or Perpetua Titling TTF
- The output file should be in .docx and in .ai.
2) Business card
- The business card will be printed in white paper and single face only, so there should be nothing on the reverse side.
3) Envelope (sizes A4, Letter, and small document)
Please refer to the picture showing some samples of stationary with designs that would fulfill our wish.
We're including the logo in .AI.
Thanks
Target Market(s)
High end investors
Industry/Entity Type
Landscape
Look and feel

```html
<!DOCTYPE html>
<html lang="en">
<head>
<meta charset="utf-8">
<title>Corvane Capital Partners — Letterhead</title>
<link href="https://fonts.googleapis.com/css2?family=Cinzel:wght@400&display=swap" rel="stylesheet">
<style>
  :root {
    --paper: #ffffff;
    --frame: #1a1a1a;
    --ink: #4d4d4f;
    --ink-soft: #5e5e60;
  }
  html, body {
    margin: 0;
    padding: 0;
    width: 845px;
    height: 1200px;
    overflow: hidden;
    background: var(--paper);
  }
  .letterhead {
    position: relative;
    width: 845px;
    height: 1200px;
    box-sizing: border-box;
    border: 2px solid var(--frame);
    background: var(--paper);
    font-family: "Cinzel", "Times New Roman", serif;
    color: var(--ink);
  }
  .company-name {
    position: absolute;
    top: 70px;
    right: 49px;
    margin: 0;
    font-size: 19px;
    line-height: 24px;
    font-weight: 400;
    color: var(--ink);
    white-space: nowrap;
  }
  .return-address {
    position: absolute;
    top: 140px;
    right: 61px;
    margin: 0;
    font-style: normal;
    text-align: right;
    font-size: 11px;
    line-height: 13.5px;
    color: var(--ink-soft);
  }
  .return-address span { display: block; }
  .return-address .group-gap { margin-top: 13.5px; }
  .return-address .wide-gap { margin-top: 54px; }
  .footer-note {
    position: absolute;
    left: 0;
    right: 0;
    top: 1126px;
    margin: 0;
    text-align: center;
    font-size: 11px;
    line-height: 13px;
    color: var(--ink-soft);
  }
</style>
</head>
<body>
  <div class="letterhead">
    <p class="company-name">Corvane Capital Partners</p>

    <address class="return-address">
      <span>Return Address</span>
      <span>Return Address - Line 2</span>
      <span>Return Address - Line 3</span>
      <span>Return Address - Line 4</span>
      <span class="group-gap">Return Address - Line 5</span>
      <span>Return Address - Line 6</span>
      <span class="group-gap">Return Address - Line 7</span>
      <span>Return Address - Line 8</span>
      <span class="wide-gap">Return Address - Line 9</span>
    </address>

    <p class="footer-note">Additional information as required or desired by Corvane Capital Partners</p>
  </div>
</body>
</html>
```